Modern Banner and Window Decal Design For Law Firm Lawyer

We are looking for three modern and sophisticated banner design and window decal for our law firm.

Banner measurements/types:

1) Height: 130 cm Width: 160 cm (Outdoor banner)
2) Height: 200 cm Width: 85 cm (Pull up/retractable indoor banner)

Window Decal:
3) Height: 70cm width 70cm

Our law firm is based in Melbourne, Australia and we deal with property law mostly.

We prefer a white background with classic text in black or grey. We would also like a dash of colour so please use a green, blue or aqua colour palette that is consistent with our logo. Vector attached. A nice photo of property, Melbourne city viee, or family home would be nice.

We do not want any law related images - scales of justice, gavel or the like.

Our ultimate goal is to communicate that the firm is modern, professional and knowledgeable

We would like the following:

1. Our logo
2. Our services: - Property Law - Wills - Powers of Attorney - Probate - Estate Administration - Consultancy & Agency
3. Phone number
4. Web Address

5. For pull up/retractable banner we would also like the following text:

We use the latest digital technology and fixed-fees to provide fast and affordable legal advice that is easy to understand.

For privacy reasons, we will provide business details once we have decided on the winner.

We will monitor entries closely and promise to provide feedback and guidance on each entry.

Thank you very much for considering this project.

Target Market(s)

General public, professionals, lawyers and conveyancers

Industry/Entity Type

Law Firm

Font styles to use
Sans Serif

Colors
0393ce
34a6d7
0456a4
3176b5
acd037
33b8a4
86cfc6
00a990
9ccb3b

Requirements
Must have
• 1. Our logo
• 2. Our services: - Property Law - Wills - Powers of Attorney - Probate & Estate Administration - Consultancy & Agency
• 3. Phone number
• 4. Web Address
Nice to have
• Picture of Melbourne, Australia city ; property/buildings/lawyers
Should not have
• We do not want any law related images - scales of justice, gavel or the like.

```html
<!DOCTYPE html>
<html lang="en">
<head>
<meta charset="utf-8">
<title>Ridgeline Lawyers – Banners</title>
<link rel="stylesheet" href="https://fonts.googleapis.com/css2?family=Oswald:wght@500&family=Cabin:wght@400;500&display=swap">
<style>
  :root {
    --accent: #6fb2d3;
    --ink: #3d3d3d;
    --panel: #77b6cd;
    --contact-bg: #4a4a4a;
    --white: #ffffff;
    --frame: #8a8a8a;
    --sky-top: #b9d9e6;
    --sky-low: #d8e7ec;
    --stone: #a9a193;
    --shadow-stone: #5d5b55;
  }
  * { margin: 0; padding: 0; box-sizing: border-box; }
  html, body { width: 1200px; height: 753px; overflow: hidden; background: var(--white); }
  body { position: relative; font-family: "Cabin", sans-serif; }

  .banner { position: absolute; background: var(--white); overflow: hidden; }
  .banner--pullup { left: 0; top: 0; width: 322px; height: 753px; border-right: 1px solid var(--frame); }
  .banner--outdoor { left: 477px; top: 155px; width: 604px; height: 492px; border: 1px solid var(--frame); }

  .contact {
    position: absolute; background: var(--contact-bg); color: var(--white);
    text-align: center; display: flex; flex-direction: column; justify-content: center;
  }
  .contact__phone { font-family: "Cabin", sans-serif; font-weight: 500; letter-spacing: 0.5px; }
  .contact__web { font-size: 8px; letter-spacing: 0.3px; }
  .banner--pullup .contact { left: 0; top: 16px; width: 136px; height: 39px; }
  .banner--pullup .contact__phone { font-size: 13px; line-height: 15px; }
  .banner--outdoor .contact { left: 410px; top: 88px; width: 193px; height: 48px; }
  .banner--outdoor .contact__phone { font-size: 17px; line-height: 20px; font-weight: 400; }
  .banner--outdoor .contact__web { font-size: 10px; }

  .brand { position: absolute; display: flex; align-items: center; gap: 8px; }
  .brand__mark { width: 36px; height: 36px; border-radius: 50%; background: var(--accent); flex: none; }
  .brand__name { font-family: "Cabin", sans-serif; font-weight: 500; color: var(--ink); font-size: 15px; line-height: 16px; letter-spacing: 0.5px; }
  .banner--pullup .brand { left: 172px; top: 17px; }
  .banner--outdoor .brand { left: 410px; top: 14px; }
  .banner--outdoor .brand__mark { width: 46px; height: 46px; }
  .banner--outdoor .brand__name { font-size: 17px; line-height: 19px; }

  .headline {
    position: absolute; font-family: "Oswald", sans-serif; font-weight: 500;
    font-size: 33px; line-height: 33px; color: var(--ink); text-transform: uppercase;
  }
  .headline__accent { color: var(--accent); }
  .banner--pullup .headline { left: 14px; top: 86px; }
  .banner--outdoor .headline { left: 26px; top: 14px; }

  .photo {
    position: absolute;
    background: linear-gradient(100deg, var(--shadow-stone) 0%, var(--stone) 30%, var(--sky-low) 55%, var(--sky-top) 100%);
  }
  .banner--pullup .photo { left: 0; top: 197px; width: 322px; height: 432px; }
  .banner--outdoor .photo { left: 0; right: 0; top: 130px; height: 298px; }

  .expertise { position: absolute; background: var(--panel); color: var(--white); text-align: center; }
  .expertise__title { font-size: 17px; font-weight: 400; letter-spacing: 0.3px; margin-bottom: 14px; }
  .expertise__list { list-style: none; }
  .expertise__item { font-size: 15px; line-height: 18px; padding-bottom: 6px; }
  .expertise__item::before {
    content: ""; display: block; margin: 0 auto 6px; width: 90px; height: 1px;
    background: linear-gradient(90deg, transparent, rgba(255,255,255,0.7), transparent);
  }
  .expertise__item:first-child::before { display: none; }
  .banner--pullup .expertise { left: 140px; top: 406px; width: 160px; height: 296px; padding-top: 16px; }
  .banner--outdoor .expertise { left: 26px; top: 174px; width: 160px; height: 296px; padding-top: 16px; }
</style>
</head>
<body>

<section class="banner banner--pullup">
  <div class="contact">
    <span class="contact__phone">555-0142-318</span>
    <span class="contact__web">RIDGELINELAWYERS.COM.AU</span>
  </div>
  <div class="brand">
    <span class="brand__mark"></span>
    <span class="brand__name">RIDGELINE<br>LAWYERS</span>
  </div>
  <h1 class="headline"><span class="headline__accent">Fast</span> and<br><span class="headline__accent">Affordable</span><br>Legal Advice.</h1>
  <div class="photo" role="img" aria-label="Melbourne clock tower with an ornate street lamp in the foreground"></div>
  <div class="expertise">
    <h2 class="expertise__title">OUR EXPERTISE</h2>
    <ul class="expertise__list">
      <li class="expertise__item">Property Law</li>
      <li class="expertise__item">Wills</li>
      <li class="expertise__item">Powers of Attorney</li>
      <li class="expertise__item">Probate</li>
      <li class="expertise__item">Estate</li>
      <li class="expertise__item">Administration</li>
      <li class="expertise__item">Consultancy<br>&amp; Agency</li>
    </ul>
  </div>
</section>

<section class="banner banner--outdoor">
  <h1 class="headline"><span class="headline__accent">Fast</span> and<br><span class="headline__accent">Affordable</span><br>Legal Advice.</h1>
  <div class="brand">
    <span class="brand__mark"></span>
    <span class="brand__name">RIDGELINE<br>LAWYERS</span>
  </div>
  <div class="photo" role="img" aria-label="Melbourne clock tower with an ornate street lamp in the foreground"></div>
  <div class="contact">
    <span class="contact__phone">555-0142-318</span>
    <span class="contact__web">RIDGELINELAWYERS.COM.AU</span>
  </div>
  <div class="expertise">
    <h2 class="expertise__title">OUR EXPERTISE</h2>
    <ul class="expertise__list">
      <li class="expertise__item">Property Law</li>
      <li class="expertise__item">Wills</li>
      <li class="expertise__item">Powers of Attorney</li>
      <li class="expertise__item">Probate</li>
      <li class="expertise__item">Estate</li>
      <li class="expertise__item">Administration</li>
      <li class="expertise__item">Consultancy<br>&amp; Agency</li>
    </ul>
  </div>
</section>

</body>
</html>
```